TRV Mechanical Solutions Business Card Design

Business card design

Thinking just large logo on one side with a phone number and the back side is contact info with services we offer with a industrial plant across the bottom of the card

See must haves. I will be laser etching these business cards on black metal business cards as well as full color card stock. So must be bold and professional.

Target Market(s)

Industrial manufacturing

Contact Information for Business Card

Industrial manufacturing construction business specializing in consulting project managment and completing projects turn key

Font styles to use
Other font styles liked:
• See Logo for colors and font style

Requirements
Must have
• TRV Mechanical Solutions
• Gerald Munroe
• 2847 Alderwick Lane
• Bel Air, MD, 21047
• Project Managment
• Consulting
• Turn Key Industrial Projects
• I’d like a industrial manufacturing “cityline” on the back side bottom of the
• I’d like to be able to print these business cards in regular color on card stock but I’d also like the design to be etched into black metal business cards

```html
<!DOCTYPE html>
<html lang="en">
<head>
<meta charset="utf-8">
<title>TRV Mechanical Solutions – Business Card</title>
<link rel="stylesheet" href="https://fonts.googleapis.com/css2?family=Lato:wght@400;700;900&display=swap">
<style>
  :root {
    --brand-blue: #2d5aa8;
    --ink-dark: #3a3a3c;
    --swoosh-grey: #4a4a4c;
    --card-white: #ffffff;
    --backdrop: #e9e9ea;
  }
  * { box-sizing: border-box; margin: 0; padding: 0; }
  html, body {
    width: 1200px;
    height: 900px;
    overflow: hidden;
    background: var(--backdrop);
    font-family: "Lato", sans-serif;
  }
  .canvas {
    position: relative;
    width: 1200px;
    height: 900px;
  }
  .card {
    position: absolute;
    left: 280px;
    width: 640px;
    height: 366px;
    overflow: hidden;
    box-shadow: 0 6px 18px rgba(0,0,0,0.18);
  }

  /* Front side */
  .card--front {
    top: 64px;
    background: var(--brand-blue);
    color: var(--card-white);
    display: flex;
    flex-direction: column;
    align-items: center;
    justify-content: center;
    gap: 30px;
  }
  .front-brand {
    display: flex;
    align-items: center;
    gap: 16px;
  }
  .front-brand__mark {
    width: 30px;
    height: 30px;
    background: var(--card-white);
  }
  .front-brand__name {
    font-weight: 700;
    font-size: 38px;
    letter-spacing: 0.5px;
  }
  .front-phone {
    font-weight: 400;
    font-size: 28px;
    letter-spacing: 1px;
  }

  /* Back side */
  .card--back {
    top: 470px;
    background: var(--card-white);
  }
  .back-wave {
    position: absolute;
    inset: 0;
    width: 640px;
    height: 366px;
  }
  .holder-name {
    position: absolute;
    left: 48px;
    top: 66px;
    font-weight: 900;
    font-size: 24px;
    letter-spacing: 0.5px;
    text-transform: uppercase;
  }
  .holder-name__first { color: var(--brand-blue); }
  .holder-name__last { color: var(--ink-dark); }

  .back-brand {
    position: absolute;
    right: 34px;
    top: 40px;
    display: flex;
    align-items: center;
    gap: 10px;
    color: var(--brand-blue);
    font-weight: 700;
    font-size: 22px;
  }
  .back-brand__mark {
    width: 18px;
    height: 18px;
    background: var(--brand-blue);
  }

  .contact-list {
    position: absolute;
    left: 48px;
    top: 150px;
    list-style: none;
    color: var(--ink-dark);
    font-size: 18px;
    line-height: 26px;
  }
  .contact-list li {
    display: flex;
    align-items: center;
    gap: 8px;
  }
  .contact-icon {
    width: 16px;
    height: 16px;
    fill: var(--brand-blue);
  }
  .service-list {
    position: absolute;
    left: 48px;
    top: 208px;
    list-style: none;
    color: var(--ink-dark);
    font-size: 18px;
    line-height: 24px;
  }
  .service-list li::before {
    content: "\25CF";
    font-size: 11px;
    margin-right: 8px;
    vertical-align: 2px;
  }
  .address {
    position: absolute;
    right: 30px;
    top: 262px;
    text-align: right;
    color: var(--card-white);
    font-size: 16px;
    font-style: normal;
    line-height: 22px;
  }
</style>
</head>
<body>
<main class="canvas">

  <section class="card card--front" aria-label="Business card front">
    <div class="front-brand">
      <span class="front-brand__mark"></span>
      <span class="front-brand__name">TRV Mechanical Solutions</span>
    </div>
    <p class="front-phone">044-555 018 274</p>
  </section>

  <section class="card card--back" aria-label="Business card back">
    <svg class="back-wave" viewBox="0 0 640 366" aria-hidden="true">
      <path d="M0,318 C160,342 340,318 480,248 C340,308 170,330 0,306 Z" fill="var(--swoosh-grey)"/>
      <path d="M0,340 C200,360 420,300 640,110 L640,366 L0,366 Z" fill="var(--brand-blue)"/>
    </svg>

    <h1 class="holder-name">
      <span class="holder-name__first">Gerald</span>
      <span class="holder-name__last">Munroe</span>
    </h1>

    <div class="back-brand">
      <span class="back-brand__mark"></span>
      <span class="back-brand__name">TRV Mechanical Solutions</span>
    </div>

    <ul class="contact-list">
      <li>
        <svg class="contact-icon" viewBox="0 0 24 24" aria-hidden="true">
          <path d="M6.6 10.8c1.4 2.8 3.8 5.1 6.6 6.6l2.2-2.2c.3-.3.7-.4 1-.2 1.1.4 2.300.6 3.6.6.6 0 1 .4 1 1V20c0 .6-.4 1-1 1C10.6 21 3 13.4 3 4c0-.6.4-1 1-1h3.5c.6 0 1 .4 1 1 0 1.3.2 2.5.6 3.6.1.3 0 .7-.2 1L6.6 10.8z"/>
        </svg>
        <span>044-555 018 274</span>
      </li>
      <li>
        <svg class="contact-icon" viewBox="0 0 24 24" aria-hidden="true">
          <path d="M2 5h20v14H2z M2 5l10 8 10-8" stroke="#fff" stroke-width="1.5"/>
        </svg>
        <span>hello@trvmech.com</span>
      </li>
    </ul>

    <ul class="service-list">
      <li>Project Managment</li>
      <li>Consulting</li>
      <li>Turn Key Industrial Projects</li>
    </ul>

    <address class="address">
      2847 Alderwick Lane<br>
      Bel Air, MD, 21047
    </address>
  </section>

</main>
</body>
</html>
```